Business Card for Managing Partner Investment Fund

To create a business card template for an investment fund manager. Business card should be more professional in nature, not too colorful, more upscale, and created using the attached logos and fund name files. I would prefer a black or gray color scheme, but am open to the use of color as well. I would prefer a double sided business card, but open to single sided business card designs as well. The business card should include: name, title, and contact information, as well as logo and company name. I would prefer a more stream-lined, simple business card design.
Updates
Address: 4136 NE 19th Ter. Ocala, FL 34470
Email: travis48@quillnet-mail.com
Phone: 561-374-9186
Title: managing partner
Name: Travis Whitlow
Fund Name: Emberfall Capital
Logos can be found in files attached to the brief
Target Market(s)
potential investors, other fund managers
Industry/Entity Type
Finance
Contact Information for Business Card
Name on card: Travis Whitlow
Title: Managing Partner
Font styles to use
Colors
Designer to choose colors to be used in the design.
Requirements
Must have
- Phone number
- email address
- physical address
- title
- name
- logo
- Fund name
Nice to have
- simple layout
Should not have
- too many colors, busy fonts,

```html
<!DOCTYPE html>
<html lang="en">
<head>
<meta charset="utf-8">
<title>Emberfall Capital – Business Card</title>
<link rel="stylesheet" href="https://fonts.googleapis.com/css2?family=Libre+Baskerville:wght@400;700&family=Open+Sans:wght@400&display=swap">
<style>
  :root {
    --page-bg: #1a1a1a;
    --card-front: #f7f7f7;
    --card-back: #4b4b4b;
    --ink-dark: #3a3a3a;
    --ink-mid: #555555;
    --ink-soft: #666666;
  }
  * { margin: 0; padding: 0; box-sizing: border-box; }
  html, body {
    width: 1200px;
    height: 864px;
    overflow: hidden;
    background: var(--page-bg);
  }
  .canvas {
    position: relative;
    width: 1200px;
    height: 864px;
  }
  .card {
    position: absolute;
    left: 320px;
    width: 560px;
    height: 320px;
    border-radius: 2px;
  }
  .card-back {
    top: 80px;
    background: linear-gradient(135deg, #555555, var(--card-back) 60%, #444444);
  }
  .card-front {
    top: 464px;
    background: radial-gradient(circle at 40% 30%, #ffffff, var(--card-front) 70%, #ececec);
    color: var(--ink-dark);
  }
  .brand {
    position: absolute;
    right: 50px;
    top: 62px;
    text-align: center;
    font-family: "Libre Baskerville", serif;
    font-weight: 400;
    color: var(--ink-mid);
    font-size: 22px;
    letter-spacing: 2px;
    line-height: 1.2;
  }
  .identity {
    position: absolute;
    left: 60px;
    top: 182px;
  }
  .person-name {
    font-family: "Libre Baskerville", serif;
    font-weight: 700;
    font-size: 17px;
    letter-spacing: 0.5px;
    text-transform: uppercase;
    color: var(--ink-dark);
  }
  .person-title {
    font-family: "Open Sans", sans-serif;
    font-size: 13px;
    color: var(--ink-soft);
    margin-top: 2px;
  }
  .contact {
    position: absolute;
    left: 52px;
    top: 240px;
    font-family: "Open Sans", sans-serif;
    font-size: 14px;
    line-height: 1.45;
    color: var(--ink-dark);
  }
  .address {
    position: absolute;
    right: 60px;
    top: 262px;
    text-align: right;
    font-family: "Open Sans", sans-serif;
    font-size: 14px;
    line-height: 1.45;
    color: var(--ink-dark);
  }
</style>
</head>
<body>
  <main class="canvas">
    <section class="card card-back" role="img" aria-label="Repeating mountain-range pattern in dark grey tones"></section>

    <section class="card card-front">
      <div class="brand">EMBERFALL<br>CAPITAL</div>

      <div class="identity">
        <h1 class="person-name">Travis Whitlow</h1>
        <p class="person-title">Managing Partner</p>
      </div>

      <div class="contact">
        <p class="phone">561-374-9186</p>
        <p class="email">travis48@quillnet-mail.com</p>
      </div>

      <address class="address" style="font-style: normal;">
        4136 NE 19th Ter.<br>Ocala, FL 34470
      </address>
    </section>
  </main>
</body>
</html>
```